I need three graphics made that will go on walls in a basketball lockerroom

I need three graphics made that will go on a basketball lockerroom wall. Here are the specifics.
Graphic 1 (Size 115" wide by 52" tall, min 150 DPI)
This should be something that displays the acronym for MARLOW. The main background color should be the teal color attached. Use logos and the other approved colors as needed.
Standards
Intensity
Effort
Grit
Energy
Love
Graphic 2 (Size 88" wide by 52" tall, min 150 DPI)
This one should be on the Navy Blue background color attached
and impactful way say Attitude and Effort
Graphic 3 (Size 100" wide by 18" tall, min 150 DPI)
This goes along the top of the way and needs to say
(MHS logo) Foxes Lead the Way (Fox logo) Marlow Basketball (MHS logo)
All three of these need to feel like they are of the same style. For Graphic #2 I thought something maybe like the attached basketball except use the M Fox in the middle and say attitude and effort using the colors .. but I'm open to other ideas

```html
<!DOCTYPE html>
<html lang="en">
<head>
<meta charset="utf-8">
<title>Marlow Basketball – Core Values Wall Graphic</title>
<link rel="stylesheet" href="https://fonts.googleapis.com/css2?family=Saira:ital,wdth,wght@0,50..125,400..900;1,50..125,400..900&display=swap">
<style>
  :root {
    --page: #f1efec;
    --navy-deep: #06132a;
    --navy: #0b1f44;
    --royal: #0d44a8;
    --teal: #0b7e8c;
    --teal-bright: #1fc4d2;
    --silver: #d6d6d8;
    --silver-dark: #9a9ea6;
    --white: #ffffff;
  }
  * { box-sizing: border-box; margin: 0; padding: 0; }
  html, body {
    width: 1200px; height: 626px; overflow: hidden;
    background: var(--page);
  }
  .canvas { position: relative; width: 1200px; height: 626px; }

  .banner {
    position: absolute; left: 46px; top: 57px;
    width: 1106px; height: 513px;
    background: var(--navy-deep);
    overflow: hidden;
  }
  .banner-art { position: absolute; inset: 0; }

  .acronym-letter {
    position: absolute; top: 150px;
    transform: translateX(-50%);
    font-family: "Saira", sans-serif;
    font-style: italic; font-weight: 800;
    font-stretch: 112%;
    font-size: 124px; line-height: 1;
    color: var(--silver);
    text-shadow: 2px 2px 0 var(--teal-bright), 4px 4px 0 var(--royal), 0 0 10px rgba(0,0,0,.5);
  }

  .team-mark {
    position: absolute; left: 561px; top: 112px;
    transform: translate(-50%, -50%);
    width: 104px; height: 104px; border-radius: 50%;
    background: var(--navy); border: 4px solid var(--teal-bright);
    display: flex; align-items: center; justify-content: center;
  }
  .team-mark-name {
    font-family: "Saira", sans-serif; font-weight: 700;
    font-size: 18px; color: var(--white); letter-spacing: 1px;
  }

  .value {
    position: absolute; top: 296px; width: 170px;
    transform: translateX(-50%);
    display: flex; flex-direction: column; align-items: center;
  }
  .value-icon {
    width: 56px; height: 62px; border-radius: 12px;
    background: var(--silver); opacity: .9;
  }
  .value-label {
    margin-top: 24px;
    font-family: "Saira", sans-serif;
    font-style: italic; font-weight: 800; font-stretch: 70%;
    font-size: 27px; line-height: 1;
    color: var(--white);
  }

  .program-name {
    position: absolute; left: 559px; top: 476px;
    transform: translateX(-50%);
    display: flex; align-items: center; gap: 14px;
    font-family: "Saira", sans-serif; font-weight: 800;
    font-size: 20px; letter-spacing: 10px; line-height: 1;
    color: var(--navy);
    white-space: nowrap;
  }
  .program-dot {
    width: 18px; height: 18px; border-radius: 50%;
    background: var(--navy);
  }
</style>
</head>
<body>
<main class="canvas">
  <section class="banner">
    <svg class="banner-art" width="1106" height="513" viewBox="0 0 1106 513">
      <defs>
        <linearGradient id="hero-grad" x1="0" y1="0" x2="1" y2="0">
          <stop offset="0" stop-color="#0a2a6e"/>
          <stop offset="0.35" stop-color="#0d44a8"/>
          <stop offset="0.7" stop-color="#0a5f86"/>
          <stop offset="1" stop-color="#0b7e8c"/>
        </linearGradient>
        <linearGradient id="glow-line" x1="0" y1="0" x2="1" y2="0">
          <stop offset="0" stop-color="#1fc4d2" stop-opacity="0"/>
          <stop offset="0.5" stop-color="#7fe6ff"/>
          <stop offset="1" stop-color="#1fc4d2" stop-opacity="0"/>
        </linearGradient>
        <linearGradient id="divider" x1="0" y1="0" x2="0" y2="1">
          <stop offset="0" stop-color="#1fc4d2" stop-opacity="0"/>
          <stop offset="0.5" stop-color="#1fc4d2"/>
          <stop offset="1" stop-color="#1fc4d2" stop-opacity="0"/>
        </linearGradient>
        <linearGradient id="band-teal" x1="0" y1="0" x2="1" y2="0">
          <stop offset="0" stop-color="#0b7e8c"/>
          <stop offset="0.5" stop-color="#1fc4d2"/>
          <stop offset="1" stop-color="#0b7e8c"/>
        </linearGradient>
      </defs>

      <rect class="hero-panel" x="0" y="0" width="1106" height="265" fill="url(#hero-grad)"
            role="img" aria-label="Faded basketball players dribbling with brush strokes and halftone dots"/>
      <rect x="380" y="262" width="340" height="3" fill="url(#glow-line)"/>

      <rect x="0" y="265" width="1106" height="160" fill="var(--navy-deep)"/>
      <g class="column-dividers" fill="url(#divider)">
        <rect x="201" y="280" width="2" height="122"/>
        <rect x="377" y="280" width="2" height="122"/>
        <rect x="553" y="280" width="2" height="122"/>
        <rect x="729" y="280" width="2" height="122"/>
        <rect x="905" y="280" width="2" height="122"/>
      </g>

      <polygon points="0,418 228,513 0,513" fill="var(--silver)"/>
      <polygon points="0,430 205,513 0,513" fill="var(--teal)"/>
      <polygon points="0,446 170,513 0,513" fill="var(--navy-deep)"/>
      <polygon points="1106,432 909,513 1106,513" fill="var(--silver)"/>
      <polygon points="1106,444 932,513 1106,513" fill="var(--teal)"/>
      <polygon points="1106,458 965,513 1106,513" fill="var(--navy-deep)"/>

      <polygon points="170,485 520,423 962,490 962,496 520,434 170,492" fill="url(#band-teal)"/>
      <polygon points="190,513 228,492 520,435 940,496 909,513" fill="var(--white)"/>
    </svg>

    <span class="acronym-letter" style="left:121px">M</span>
    <span class="acronym-letter" style="left:298px">A</span>
    <span class="acronym-letter" style="left:470px">R</span>
    <span class="acronym-letter" style="left:647px">L</span>
    <span class="acronym-letter" style="left:822px">O</span>
    <span class="acronym-letter" style="left:994px">W</span>

    <div class="team-mark"><span class="team-mark-name">MARLOW</span></div>

    <div class="value" style="left:116px"><div class="value-icon" role="img" aria-label="Award ribbon with gear icon"></div><span class="value-label">STANDARDS</span></div>
    <div class="value" style="left:291px"><div class="value-icon" role="img" aria-label="Sprinting athlete icon"></div><span class="value-label">INTENSITY</span></div>
    <div class="value" style="left:467px"><div class="value-icon" role="img" aria-label="Runner climbing steps to a flag icon"></div><span class="value-label">EFFORT</span></div>
    <div class="value" style="left:643px"><div class="value-icon" role="img" aria-label="Raised fist on a shield icon"></div><span class="value-label">GRIT</span></div>
    <div class="value" style="left:818px"><div class="value-icon" role="img" aria-label="Leaping runner icon"></div><span class="value-label">ENERGY</span></div>
    <div class="value" style="left:994px"><div class="value-icon" role="img" aria-label="Team group with heart icon"></div><span class="value-label">LOVE</span></div>

    <div class="program-name">
      <span>MARLOW</span><span class="program-dot"></span><span>BASKETBALL</span>
    </div>
  </section>
</main>
</body>
</html>
```